Slider images for online fax service homepage

Qlipo® needs 4 slider images for our newly designed homepage. The slider images should convey professionalism and simplicity without feeling cold or stuffy. The 4th slide is the only one that will contain a video and should be designed with that in mind. Attached to this contest, you will find two .pdf files. One contains a mockup of the new homepage containing dimensions and font requirements. The other is a spreadsheet containing copy for each slide.
In case you are unfamiliar with the brand, Qlipo® is the industry leader in online fax services. We provide faxing capabilities from mobile phones, tablets, and computers with state-of-the-art functionality, such as the ability to sign documents with your finger and send a document to any fax number directly from email.
Updates

FYI:  The dimensions of the video are 640x360.

Hello designers,

We don't want you to think we've forgotten about this contest.  We've been delayed in user testing but hope to have a response soon.

Thank you.

Target Market(s)

Mobile professionals and small businesses who need 24/7 access to fax services, such as lawyers, realtors, truckers, etc.

Industry/Entity Type

Industry

Requirements
Must have
• • The final deliverable should consist of a layered .psd file.
• Dimensions : 1500x475 (viewable area is 1200x475)
• Font is Google font – Lato
• Headline 62pt
• Subhead 32 pt

```html
<!DOCTYPE html>
<html lang="en">
<head>
<meta charset="utf-8">
<title>Faxing without a fax machine</title>
<link rel="stylesheet" href="https://fonts.googleapis.com/css2?family=Lato:wght@300;900&display=swap">
<style>
  :root {
    --bg-violet: #4b3a8e;
    --bg-plum: #55287a;
    --bg-teal: #66aeb6;
    --bg-haze: #7f93c2;
    --bg-mist: #9c9ac0;
    --ink-white: #ffffff;
    --accent-pink: #e545c4;
    --play-magenta: rgba(222, 48, 214, 0.82);
    --bar-lavender: rgba(196, 188, 220, 0.8);
    --track-white: #ffffff;
    --icon-grey: #6e6a86;
  }
  html, body {
    margin: 0;
    padding: 0;
    overflow: hidden;
  }
  .hero {
    position: relative;
    width: 1200px;
    height: 381px;
    overflow: hidden;
    background:
      radial-gradient(ellipse 540px 300px at 1060px 50px, var(--bg-teal), transparent 75%),
      radial-gradient(ellipse 520px 250px at 620px 30px, var(--bg-haze), transparent 75%),
      radial-gradient(ellipse 440px 260px at 40px 350px, var(--bg-plum), transparent 80%),
      radial-gradient(ellipse 620px 240px at 880px 390px, var(--bg-mist), transparent 80%),
      linear-gradient(100deg, var(--bg-violet) 0%, #5d5e9e 45%, #5f97ad 100%);
    font-family: "Lato", sans-serif;
  }
  .headline {
    position: absolute;
    top: 25px;
    left: 0;
    width: 100%;
    margin: 0;
    text-align: center;
    color: var(--ink-white);
    font-size: 49px;
    font-weight: 300;
    line-height: 56px;
    letter-spacing: 0.4px;
    text-transform: uppercase;
  }
  .headline strong {
    font-weight: 900;
  }
  .players {
    position: absolute;
    left: 0;
    top: 0;
  }
</style>
</head>
<body>
<main class="hero">
  <h1 class="headline">Faxing <strong>without</strong> a fax <strong>machine.</strong></h1>

  <svg class="players" width="1200" height="381" viewBox="0 0 1200 381">
    <defs>
      <!-- meadow scene tones -->
      <linearGradient id="meadow-base" x1="0" y1="0" x2="0.4" y2="1">
        <stop offset="0" stop-color="#f2eea8"/>
        <stop offset="0.35" stop-color="#b9d46a"/>
        <stop offset="0.75" stop-color="#7fb446"/>
        <stop offset="1" stop-color="#5e9634"/>
      </linearGradient>
      <radialGradient id="meadow-glow" cx="0.15" cy="0.1" r="0.6">
        <stop offset="0" stop-color="#fffbe0" stop-opacity="0.95"/>
        <stop offset="1" stop-color="#fffbe0" stop-opacity="0"/>
      </radialGradient>
      <radialGradient id="meadow-figure" cx="0.45" cy="0.65" r="0.35">
        <stop offset="0" stop-color="#f1c4bd" stop-opacity="0.9"/>
        <stop offset="0.6" stop-color="#c9a285" stop-opacity="0.45"/>
        <stop offset="1" stop-color="#c9a285" stop-opacity="0"/>
      </radialGradient>

      <!-- toy scene tones -->
      <linearGradient id="toys-base" x1="0" y1="0" x2="1" y2="0">
        <stop offset="0" stop-color="#6e4234"/>
        <stop offset="0.3" stop-color="#c8693a"/>
        <stop offset="0.55" stop-color="#d98a64"/>
        <stop offset="0.8" stop-color="#d6a2b4"/>
        <stop offset="1" stop-color="#b5b98e"/>
      </linearGradient>
      <radialGradient id="toys-warm" cx="0.3" cy="0.55" r="0.35">
        <stop offset="0" stop-color="#f0a358" stop-opacity="0.9"/>
        <stop offset="1" stop-color="#f0a358" stop-opacity="0"/>
      </radialGradient>
      <radialGradient id="toys-cream" cx="0.4" cy="0.82" r="0.25">
        <stop offset="0" stop-color="#fbe6cf" stop-opacity="0.85"/>
        <stop offset="1" stop-color="#fbe6cf" stop-opacity="0"/>
      </radialGradient>
      <radialGradient id="toys-bokeh" cx="0.8" cy="0.45" r="0.35">
        <stop offset="0" stop-color="#e9a9d6" stop-opacity="0.8"/>
        <stop offset="1" stop-color="#e9a9d6" stop-opacity="0"/>
      </radialGradient>
      <radialGradient id="toys-leaf" cx="0.95" cy="0.05" r="0.3">
        <stop offset="0" stop-color="#5fae6e" stop-opacity="0.85"/>
        <stop offset="1" stop-color="#5fae6e" stop-opacity="0"/>
      </radialGradient>
      <linearGradient id="toys-shade" x1="0" y1="0" x2="0" y2="1">
        <stop offset="0.6" stop-color="#2a1620" stop-opacity="0"/>
        <stop offset="1" stop-color="#2a1620" stop-opacity="0.45"/>
      </linearGradient>

      <!-- treat scene tones -->
      <linearGradient id="treat-base" x1="0" y1="0" x2="1" y2="1">
        <stop offset="0" stop-color="#7c6266"/>
        <stop offset="0.45" stop-color="#c9b1b0"/>
        <stop offset="1" stop-color="#6f5a5c"/>
      </linearGradient>
      <radialGradient id="treat-sweet" cx="0.5" cy="0.4" r="0.32">
        <stop offset="0" stop-color="#f6e9e8" stop-opacity="0.9"/>
        <stop offset="0.6" stop-color="#d45a62" stop-opacity="0.45"/>
        <stop offset="1" stop-color="#d45a62" stop-opacity="0"/>
      </radialGradient>
      <radialGradient id="treat-cocoa" cx="0.75" cy="0.78" r="0.35">
        <stop offset="0" stop-color="#5a3a34" stop-opacity="0.85"/>
        <stop offset="1" stop-color="#5a3a34" stop-opacity="0"/>
      </radialGradient>

      <clipPath id="clip-left"><polygon points="192,173 373,120 373,308 192,306"/></clipPath>
      <clipPath id="clip-main"><rect x="397" y="117" width="409" height="193"/></clipPath>
      <clipPath id="clip-right"><polygon points="833,122 1005,160 1005,306 833,306"/></clipPath>

      <filter id="panel-shadow" x="-10%" y="-10%" width="120%" height="130%">
        <feDropShadow dx="0" dy="6" stdDeviation="8" flood-color="#1e1440" flood-opacity="0.35"/>
      </filter>
    </defs>

    <!-- left player -->
    <g class="player player--left" filter="url(#panel-shadow)">
      <g role="img" aria-label="Photo of a woman in a sun hat sitting in a sunny green meadow" clip-path="url(#clip-left)">
        <rect x="192" y="120" width="181" height="190" fill="url(#meadow-base)"/>
        <rect x="192" y="120" width="181" height="190" fill="url(#meadow-glow)"/>
        <rect x="192" y="120" width="181" height="190" fill="url(#meadow-figure)"/>
      </g>
      <polygon class="control-bar" points="192,306 373,308 373,338 192,324" fill="var(--bar-lavender)"/>
      <rect x="197" y="312" width="2" height="7" fill="var(--icon-grey)"/>
      <line x1="204" y1="317" x2="340" y2="320" stroke="var(--track-white)" stroke-width="4" stroke-linecap="round"/>
      <line x1="204" y1="317" x2="276" y2="318.5" stroke="var(--accent-pink)" stroke-width="4" stroke-linecap="round"/>
      <path d="M352 320 h4 l5 -5 v14 l-5 -5 h-4z" fill="none" stroke="var(--icon-grey)" stroke-width="1.2"/>
      <circle cx="264" cy="230" r="14" fill="var(--play-magenta)"/>
      <path d="M261 225 l8 5 l-8 5z" fill="none" stroke="var(--ink-white)" stroke-width="1.3"/>
    </g>

    <!-- main player -->
    <g class="player player--main" filter="url(#panel-shadow)">
      <g role="img" aria-label="Photo of two vintage toy figures holding ice cream cones with soft heart-shaped lights behind them" clip-path="url(#clip-main)">
        <rect x="397" y="117" width="409" height="193" fill="url(#toys-base)"/>
        <rect x="397" y="117" width="409" height="193" fill="url(#toys-warm)"/>
        <rect x="397" y="117" width="409" height="193" fill="url(#toys-cream)"/>
        <rect x="397" y="117" width="409" height="193" fill="url(#toys-bokeh)"/>
        <rect x="397" y="117" width="409" height="193" fill="url(#toys-leaf)"/>
        <rect x="397" y="117" width="409" height="193" fill="url(#toys-shade)"/>
      </g>
      <rect class="control-bar" x="397" y="310" width="409" height="30" fill="var(--bar-lavender)"/>
      <rect x="425" y="319" width="3" height="10" fill="var(--icon-grey)"/>
      <rect x="431" y="319" width="3" height="10" fill="var(--icon-grey)"/>
      <line x1="447" y1="324.5" x2="743" y2="324.5" stroke="var(--track-white)" stroke-width="7" stroke-linecap="round"/>
      <line x1="447" y1="324.5" x2="622" y2="324.5" stroke="var(--accent-pink)" stroke-width="7" stroke-linecap="round"/>
      <path d="M762 321 h5 l7 -6 v19 l-7 -6 h-5z" fill="none" stroke="var(--icon-grey)" stroke-width="1.5"/>
      <path d="M778 320 q4 4.5 0 9 M781 317 q7 7.5 0 15" fill="none" stroke="var(--icon-grey)" stroke-width="1.3"/>
      <circle cx="603" cy="215" r="27" fill="var(--play-magenta)"/>
      <path d="M597 207 l14 8 l-14 8z" fill="none" stroke="var(--ink-white)" stroke-width="2"/>
    </g>

    <!-- right player -->
    <g class="player player--right" filter="url(#panel-shadow)">
      <g role="img" aria-label="Photo of a hand holding a chocolate treat topped with white icing and red heart sprinkles" clip-path="url(#clip-right)">
        <rect x="833" y="122" width="172" height="184" fill="url(#treat-base)"/>
        <rect x="833" y="122" width="172" height="184" fill="url(#treat-sweet)"/>
        <rect x="833" y="122" width="172" height="184" fill="url(#treat-cocoa)"/>
      </g>
      <polygon class="control-bar" points="833,306 1005,306 1005,327 833,338" fill="var(--bar-lavender)"/>
      <rect x="842" y="317" width="2" height="9" fill="var(--icon-grey)"/>
      <rect x="846" y="317" width="2" height="9" fill="var(--icon-grey)"/>
      <line x1="853" y1="321.5" x2="988" y2="318" stroke="var(--track-white)" stroke-width="5" stroke-linecap="round"/>
      <line x1="853" y1="321.5" x2="940" y2="319.3" stroke="var(--accent-pink)" stroke-width="5" stroke-linecap="round"/>
      <path d="M994 318 h3 l4 -4 v11 l-4 -4 h-3z" fill="none" stroke="var(--icon-grey)" stroke-width="1.1"/>
      <circle cx="929" cy="225" r="14" fill="var(--play-magenta)"/>
      <path d="M926 220 l8 5 l-8 5z" fill="none" stroke="var(--ink-white)" stroke-width="1.3"/>
    </g>
  </svg>
</main>
</body>
</html>
```